wealth management firm, professional group, new model

we have a logo that works but we need a card, white background using our colors...clean look

our tag line if can be used in

The Path From Saver to Investor

```html
<!DOCTYPE html>
<html lang="en">
<head>
<meta charset="utf-8">
<title>Calder Wealth Partners — Business Card</title>
<link href="https://fonts.googleapis.com/css2?family=Jost:wght@400;500;600&display=swap" rel="stylesheet">
<style>
  :root {
    --navy: #14284b;
    --grey-text: #555a60;
    --paper: #ffffff;
    --backdrop: #ebebeb;
  }
  * { margin: 0; padding: 0; box-sizing: border-box; }
  html, body { width: 1200px; height: 1000px; overflow: hidden; }
  body {
    position: relative;
    background: var(--backdrop);
    font-family: "Jost", "Futura", sans-serif;
    color: var(--navy);
  }
  .card {
    position: absolute;
    left: 254px;
    width: 693px;
    height: 396px;
    background: var(--paper);
  }
  .card--front { top: 78px; }
  .card--back { top: 526px; }
  .card__frame {
    position: absolute;
    left: 15px; top: 15px; right: 15px; bottom: 15px;
    border: 3px solid var(--navy);
  }

  /* front */
  .identity {
    position: absolute;
    right: 393px;
    top: 174px;
    text-align: right;
  }
  .identity__name {
    font-weight: 600;
    font-size: 29px;
    line-height: 1;
    letter-spacing: 0.2px;
  }
  .identity__title {
    margin-top: 4px;
    font-size: 17.5px;
    color: var(--grey-text);
  }
  .divider {
    position: absolute;
    left: 332px;
    top: 119px;
    width: 2px;
    height: 161px;
    background: var(--navy);
  }
  .contact {
    position: absolute;
    left: 365px;
    top: 115px;
    list-style: none;
  }
  .contact__item {
    position: relative;
    padding-left: 22px;
    font-size: 16.5px;
    line-height: 24px;
    color: var(--grey-text);
    letter-spacing: 0.3px;
  }
  .contact__item--address { line-height: 21px; margin-bottom: 8px; }
  .contact__item--phone { font-size: 18px; }
  .contact__item svg {
    position: absolute;
    left: 0; top: 6px;
    width: 13px; height: 13px;
    fill: var(--navy);
  }
  .contact__item--address svg { top: 4px; }

  /* back */
  .brand {
    position: absolute;
    left: 0; right: 0;
    top: 172px;
    text-align: center;
    font-weight: 400;
  }
  .brand__name {
    font-size: 54px;
    line-height: 1;
    letter-spacing: 27px;
    margin-right: -27px;
  }
  .brand__sub {
    margin-top: 30px;
    font-size: 23px;
    letter-spacing: 4.6px;
    margin-right: -4.6px;
  }
  .tagline {
    position: absolute;
    left: 0; right: 0;
    top: 332px;
    text-align: center;
    font-size: 18px;
    letter-spacing: 1px;
  }
</style>
</head>
<body>

<section class="card card--front">
  <div class="card__frame"></div>

  <div class="identity">
    <p class="identity__name">DANIEL REYES</p>
    <p class="identity__title">Founder &amp; CEO</p>
  </div>

  <div class="divider"></div>

  <ul class="contact">
    <li class="contact__item contact__item--address">
      <svg viewBox="0 0 16 16" aria-hidden="true"><path d="M8 0a5.5 5.5 0 0 0-5.5 5.5C2.5 10 8 16 8 16s5.5-6 5.5-10.5A5.5 5.5 0 0 0 8 0zm0 8a2.5 2.5 0 1 1 0-5 2.5 2.5 0 0 1 0 5z"/></svg>
      Street Address Here, City<br>State, Country, ZIP 123
    </li>
    <li class="contact__item contact__item--phone">
      <svg viewBox="0 0 16 16" aria-hidden="true"><path d="M3.5 1l2.5 3-1.5 2c.9 2 2.5 3.6 4.5 4.5l2-1.5 3 2.5-1.5 3C7 14.5 1.5 9 1 2.5z"/></svg>
      (123) 456-7890
    </li>
    <li class="contact__item contact__item--phone">
      <svg viewBox="0 0 16 16" aria-hidden="true"><path d="M4 0h8a1 1 0 0 1 1 1v14a1 1 0 0 1-1 1H4a1 1 0 0 1-1-1V1a1 1 0 0 1 1-1zm1 2v10h6V2zm3 11a1 1 0 1 0 0 2 1 1 0 0 0 0-2z"/></svg>
      (123) 456-7890
    </li>
    <li class="contact__item contact__item--phone">
      <svg viewBox="0 0 16 16" aria-hidden="true"><path d="M4 0h8v4H4zM1 5h14v7h-3v4H4v-4H1zm4 5v4h6v-4z"/></svg>
      (123) 456-7890
    </li>
    <li class="contact__item">
      <svg viewBox="0 0 16 16" aria-hidden="true"><path d="M0 3h16v1L8 9 0 4zm0 2.5l8 5 8-5V13H0z"/></svg>
      info@yourwebsitehere.com
    </li>
    <li class="contact__item">
      <svg viewBox="0 0 16 16" aria-hidden="true"><path d="M8 0a8 8 0 1 0 0 16A8 8 0 0 0 8 0zm-1 2.2C5.5 3.5 5 4.5 6 5.5s2 0 2.5 1.5-1.5 2-1 3.5 1 2.5.5 3.4A6 6 0 0 1 7 2.2zm3 .5a6 6 0 0 1 3.5 7c-1-.7-1.5-2-2.5-2.2S9 6 10 5s0-1.5 0-2.3z"/></svg>
      yourwebsitehere.com
    </li>
  </ul>
</section>

<section class="card card--back">
  <div class="card__frame"></div>

  <div class="brand">
    <p class="brand__name">CALDER</p>
    <p class="brand__sub">WEALTH PARTNERS</p>
  </div>

  <p class="tagline">THE PATH FROM SAVER TO INVESTOR</p>
</section>

</body>
</html>
```